See a product example for AI Sales Assistant tool - High Converting Marketing page

When a potential customer visits our site, they will be driven to this page where they can see how our product works. The goal of this page is to allow a potential customer to picture how ovaMerrit, our product, fits into their business processes and tools. We will do this by using an example customer, which is Gideon the owner of a small painting business and how he uses ovaMerrit.
Page will have 3 basic components:
1. Example customer persona with image (e.g. I'm Gideon the owner of a small painting business and I use ovaMerrit to do this...)
2. Interactive examples of the ovaMerrit product using the Gideon the Painter example
3. A button to sign up now

Please check out the word doc uploaded here as well for the details of this project.

```html
<!DOCTYPE html>
<html lang="en">
<head>
<meta charset="utf-8">
<title>ovaMerrit – Product Example</title>
<link href="https://fonts.googleapis.com/css2?family=Inter:wght@400;500;600;700;800&display=swap" rel="stylesheet">
<style>
:root{
  --purple:#9a5b9c;
  --violet:#6b4d9a;
  --teal:#16687c;
  --teal-dark:#12505f;
  --yellow:#fdd267;
  --ink:#1f1f2b;
  --text:#2c2c36;
  --muted:#8a8a94;
  --white:#ffffff;
  --dot:#b9bcc6;
  --sky:#5fc3e0;
  --sky-deep:#2f97c2;
}
*{box-sizing:border-box;margin:0;padding:0}
html,body{width:1200px;height:4286px;overflow:hidden;background:var(--white)}
body{position:relative;font-family:"Inter",sans-serif;color:var(--text)}
.abs{position:absolute}
.brand{font-weight:800;letter-spacing:-.5px}

/* buttons */
.btn{position:absolute;display:flex;align-items:center;gap:14px;padding-left:22px;background:var(--yellow);color:var(--ink);font-weight:700;font-size:17px;border-radius:3px;white-space:nowrap}
.btn .arrow{width:28px;height:28px;border-radius:50%;background:var(--white);display:flex;align-items:center;justify-content:center;flex:none}

/* mascot placeholder */
.mascot{position:absolute;border-radius:50% 50% 44% 44% / 46% 46% 54% 54%;background:radial-gradient(circle at 50% 30%,#bdeefa 0%,var(--sky) 40%,var(--sky-deep) 100%);box-shadow:inset 0 -10px 0 rgba(20,80,120,.18)}

/* hero */
.hero{position:absolute;left:0;top:0;width:1200px;height:658px;background:linear-gradient(100deg,var(--purple) 0%,#7d5a98 40%,#35607f 75%,var(--teal) 100%);overflow:hidden}
.hero .brand{left:106px;top:46px;font-size:40px;color:var(--white)}
.nav a{position:absolute;top:60px;font-size:17px;font-weight:600;color:var(--white);text-decoration:none}
.nav .login{border-bottom:2px solid var(--white);padding-bottom:6px}
.hero-welcome{left:106px;top:234px;font-size:32px;color:var(--white)}
.hero-title{left:104px;top:262px;font-size:70px;font-weight:800;color:var(--white);letter-spacing:-1px}
.hero-sub{left:106px;top:346px;font-size:31px;font-weight:700;color:var(--white);line-height:40px}
.ring{left:633px;top:158px;width:432px;height:432px;border-radius:50%;border:16px solid rgba(255,255,255,.12);background:radial-gradient(circle,#1a5766 0%,#1b5a6c 62%,transparent 63%)}
.phone{left:734px;top:150px;width:228px;height:462px;border-radius:30px;background:var(--white);padding:8px}
.screen{width:100%;height:100%;border-radius:24px;background:#e9edf3;overflow:hidden;position:relative}
.screen-head{height:76px;background:var(--teal-dark);display:flex;align-items:center;gap:10px;padding:12px 14px 0}
.avatar{width:30px;height:30px;border-radius:50%;background:#f0b9a7;flex:none}
.bot{width:30px;height:30px;border-radius:50%;background:radial-gradient(circle at 50% 35%,#bdeefa,var(--sky) 50%,var(--sky-deep));flex:none}
.screen-head b{display:block;color:var(--white);font-size:12px}
.screen-head span{color:#d7e6ea;font-size:10px}
.msg{position:absolute;font-size:9.5px;line-height:12px;padding:6px 9px;border-radius:4px}
.msg.in{background:var(--white);color:#444}
.msg.out{background:#7d5aa8;color:var(--white)}
.screen-input{position:absolute;left:12px;right:12px;bottom:12px;height:30px;border-radius:4px;background:#d6dde6;font-size:10px;color:#555;padding:9px 10px}

/* features */
.num{font-size:17px;font-weight:600;color:var(--muted)}
.feat-title{font-size:38px;font-weight:700;color:var(--ink);letter-spacing:-.5px}
.rule{width:62px;height:4px;background:var(--yellow)}
.feat-name{font-size:25px;font-weight:500;color:var(--violet)}
.feat-desc{font-size:21px;line-height:32px;color:var(--text)}
.media{position:absolute;border-radius:3px}
.dots{position:absolute;border:3px dotted var(--dot);border-radius:2px}
.device{position:absolute;border-radius:14px;background:#1e1e22;padding:12px;box-shadow:0 6px 18px rgba(0,0,0,.15)}
.device .fill{position:relative;width:100%;height:100%;border-radius:6px;overflow:hidden}
.chat-card{position:absolute;background:linear-gradient(120deg,#2b9bb4,#6a56a2);border-radius:4px}
.pill{position:absolute;background:var(--white);border-radius:8px;font-size:13px;color:#333;padding:7px 12px;white-space:nowrap}
.callpill{position:absolute;background:var(--white);border-radius:22px;display:flex;align-items:center;gap:10px;padding:6px 16px;font-size:13px;color:#333;line-height:14px}
.callpill b{color:#2c82c9;font-weight:700;font-size:14px}
.owl-badge{position:absolute;border-radius:50%;background:#1f4f63;border:5px solid var(--white);box-shadow:0 4px 12px rgba(0,0,0,.2)}
.owl-badge .mascot{left:26%;top:18%;width:48%;height:64%}
.icon-tile{position:absolute;border-radius:3px;display:flex;align-items:center;justify-content:center}

/* feed screen */
.feed{background:#f6f7fa}
.feed .bar{position:absolute;height:6px;border-radius:3px;background:#cfd3dc}
.feed .dot{position:absolute;width:12px;height:12px;border-radius:50%}
.feed .tile{position:absolute;border-radius:3px}

/* cta */
.cta{position:absolute;left:0;top:3310px;width:1200px;height:446px;background:linear-gradient(100deg,var(--purple),#5a5791 55%,var(--teal))}
.cta h2{position:absolute;top:100px;width:100%;text-align:center;font-size:36px;font-weight:700;color:var(--white)}
.cta .rule{position:absolute;left:567px;top:162px}

/* footer */
.footer-brand{left:0;width:1200px;top:3850px;text-align:center;font-size:44px;color:var(--violet)}
.footer-nav a{position:absolute;top:3942px;font-size:17px;color:var(--ink);text-decoration:none}
.social{position:absolute;top:3999px;width:70px;height:70px;border-radius:50%;background:#c8eff7;display:flex;align-items:center;justify-content:center;font-size:12px;font-weight:600;color:var(--ink)}
.feedback{left:0;width:1200px;top:4103px;text-align:center;font-size:17px;color:var(--muted)}
.feedback span{color:var(--ink)}
.legal{top:4203px;font-size:13px;color:#555}
.legal b{color:var(--violet)}
.stamp{top:4203px;right:106px;font-size:13px;color:#b0b0b8}
</style>
</head>
<body>

<header class="hero">
  <div class="abs brand">ovaMerrit!</div>
  <nav class="nav">
    <a href="#" style="left:420px">Home</a>
    <a href="#" style="left:522px">Product</a>
    <a href="#" style="left:643px">News &amp; Blog</a>
    <a href="#" class="login" style="left:849px">Log In</a>
  </nav>
  <div class="btn" style="left:927px;top:43px;width:165px;height:60px">
    <span class="arrow"><svg width="14" height="14" viewBox="0 0 14 14"><path d="M2 7h10M8 3l4 4-4 4" stroke="#333" stroke-width="1.6" fill="none"/></svg></span>Sign Up
  </div>
  <div class="abs hero-welcome">Welcome To!</div>
  <div class="abs hero-title">Hey Merrit</div>
  <div class="abs hero-sub">Get Help Business Processes<br>And Tools</div>
  <div class="btn" style="left:106px;top:464px;width:242px;height:62px">
    <span class="arrow"><svg width="14" height="14" viewBox="0 0 14 14"><path d="M2 7h10M8 3l4 4-4 4" stroke="#333" stroke-width="1.6" fill="none"/></svg></span>Get Started Now
  </div>
  <div class="abs ring"></div>
  <div class="mascot" role="img" aria-label="Blue owl mascot with round glasses" style="left:610px;top:300px;width:80px;height:118px"></div>
  <div class="abs phone">
    <div class="screen">
      <div class="screen-head"><div class="avatar"></div><div><b>Gideon Hale</b><span>Owner Of Painting Business</span></div></div>
      <div class="msg in" style="left:72px;top:96px;width:124px">Hi Gideon! how can I help you?</div>
      <div class="bot abs" style="left:20px;top:114px;width:26px;height:26px"></div>
      <div class="msg out" style="left:14px;top:166px;width:124px">Which painting is good for business?</div>
      <div class="avatar abs" style="left:166px;top:186px;width:26px;height:26px"></div>
      <div class="msg in" style="left:78px;top:240px;width:118px">A waterfall painting signifies</div>
      <div class="bot abs" style="left:20px;top:262px;width:26px;height:26px"></div>
      <div class="msg out" style="left:14px;top:314px;width:124px">I'm planning my son's wedding.Can you help ?</div>
      <div class="avatar abs" style="left:166px;top:334px;width:26px;height:26px"></div>
      <div class="screen-input">Type your response ...</div>
    </div>
  </div>
</header>

<!-- 01 Chat -->
<div class="dots" style="left:326px;top:990px;width:258px;height:176px;border-left:none;border-top:none"></div>
<div class="device" style="left:106px;top:769px;width:445px;height:338px">
  <div class="fill feed">
    <div class="bar" style="left:0;top:0;width:100%;height:18px;border-radius:0;background:#fff"></div>
    <div class="dot" style="left:10px;top:30px;background:#e3a27b"></div><div class="bar" style="left:28px;top:33px;width:40px"></div>
    <div class="dot" style="left:10px;top:52px;background:#4a7ccf"></div><div class="bar" style="left:28px;top:55px;width:36px"></div>
    <div class="dot" style="left:10px;top:74px;background:#4aa0d8"></div><div class="bar" style="left:28px;top:77px;width:30px"></div>
    <div class="dot" style="left:10px;top:96px;background:#c757b5"></div><div class="bar" style="left:28px;top:99px;width:34px"></div>
    <div class="dot" style="left:10px;top:118px;background:#4c4c55"></div><div class="bar" style="left:28px;top:121px;width:32px"></div>
    <div class="dot" style="left:10px;top:140px;background:#7a7a84"></div><div class="bar" style="left:28px;top:143px;width:28px"></div>
    <div class="dot" style="left:10px;top:162px;background:#f08a3c"></div><div class="bar" style="left:28px;top:165px;width:30px"></div>
    <div class="dot" style="left:10px;top:184px;background:#3fb56a"></div><div class="bar" style="left:28px;top:187px;width:38px"></div>
    <div class="tile" role="img" aria-label="Row of story photos" style="left:104px;top:26px;width:198px;height:72px;background:linear-gradient(90deg,#3b3b44 0%,#e0c23e 20%,#c84b5a 45%,#7a4bb3 62%,#d9c9b8 80%,#4a4a52 100%)"></div>
    <div class="tile" style="left:104px;top:106px;width:198px;height:26px;background:#fff"></div>
    <div class="tile" style="left:104px;top:140px;width:198px;height:26px;background:#fff"></div>
    <div class="tile" role="img" aria-label="Beach resort photo post" style="left:104px;top:170px;width:198px;height:96px;background:linear-gradient(180deg,#f5d7a8 0%,#f2b67a 45%,#6fb2c8 70%,#2f6f85 100%)"></div>
    <div class="tile" style="left:104px;top:272px;width:198px;height:40px;background:#fff"></div>
    <div class="bar" style="left:316px;top:30px;width:56px"></div>
    <div class="dot" style="left:316px;top:46px;background:#e3a27b"></div><div class="bar" style="left:334px;top:49px;width:50px"></div>
    <div class="dot" style="left:316px;top:66px;background:#c98f6e"></div><div class="bar" style="left:334px;top:69px;width:56px"></div>
    <div class="dot" style="left:316px;top:86px;background:#8a6a5a"></div><div class="bar" style="left:334px;top:89px;width:52px"></div>
    <div class="dot" style="left:316px;top:106px;background:#d9b79c"></div><div class="bar" style="left:334px;top:109px;width:48px"></div>
    <div class="dot" style="left:316px;top:126px;background:#b5473a"></div><div class="bar" style="left:334px;top:129px;width:38px"></div>
    <div class="dot" style="left:316px;top:146px;background:#6e5a52"></div><div class="bar" style="left:334px;top:149px;width:50px"></div>
    <div class="dot" style="left:316px;top:166px;background:#8c8c92"></div><div class="bar" style="left:334px;top:169px;width:44px"></div>
  </div>
</div>
<div class="chat-card" style="left:374px;top:1052px;width:237px;height:138px">
  <div class="pill" style="right:20px;top:24px">Hey,Whats up</div>
  <div class="bot abs" style="left:12px;top:70px;width:32px;height:32px;border:2px solid #fff"></div>
  <div class="pill" style="left:56px;top:70px">I'm good.. Hows your day</div>
</div>
<div class="abs num" style="left:696px;top:784px">01</div>
<div class="abs feat-title" style="left:696px;top:808px">Chat</div>
<div class="abs rule" style="left:696px;top:862px"></div>
<div class="abs feat-name" style="left:696px;top:900px">ovaMerrit</div>
<div class="abs feat-desc" style="left:696px;top:934px;width:385px">Chat on my website and add it as my link in bio on social media.</div>
<div class="btn" style="left:696px;top:1023px;width:196px;height:59px">
  <span class="arrow"><svg width="14" height="14" viewBox="0 0 14 14"><path d="M2 7h10M8 3l4 4-4 4" stroke="#333" stroke-width="1.6" fill="none"/></svg></span>Try Out Chat
</div>

<!-- 02 Phone Calls -->
<div class="abs num" style="left:106px;top:1316px">02</div>
<div class="abs feat-title" style="left:106px;top:1346px">Phone Calls</div>
<div class="abs rule" style="left:106px;top:1401px"></div>
<div class="abs feat-name" style="left:106px;top:1438px">Merrit</div>
<div class="abs feat-desc" style="left:106px;top:1474px">answers my phone calls</div>
<div class="btn" style="left:106px;top:1534px;width:197px;height:58px">
  <span class="arrow"><svg width="14" height="14" viewBox="0 0 14 14"><path d="M2 7h10M8 3l4 4-4 4" stroke="#333" stroke-width="1.6" fill="none"/></svg></span>Listen To Call
</div>
<div class="dots" style="left:558px;top:1316px;width:522px;height:356px;border-right:none"></div>
<div class="media" role="img" aria-label="White passenger van driving on a sunny road" style="left:579px;top:1326px;width:479px;height:326px;background:radial-gradient(ellipse 45% 40% at 55% 52%,#eeeae2 0%,#d8d3c8 45%,transparent 75%),linear-gradient(180deg,#9fb4bd 0%,#c7bca4 38%,#b7a98f 55%,#57534d 78%,#2f2d2a 100%)"></div>
<div class="callpill" style="left:634px;top:1340px;width:178px;height:41px">
  <svg width="16" height="16" viewBox="0 0 24 24"><path d="M6.6 10.8a15 15 0 0 0 6.6 6.6l2.2-2.2a1 1 0 0 1 1-.25 11 11 0 0 0 3.6.6 1 1 0 0 1 1 1V20a1 1 0 0 1-1 1A17 17 0 0 1 3 4a1 1 0 0 1 1-1h3.5a1 1 0 0 1 1 1c0 1.25.2 2.45.6 3.6a1 1 0 0 1-.25 1z" fill="#333"/></svg>
  <div>calling from<br><b>310-555-0147</b></div>
</div>
<div class="icon-tile" style="left:943px;top:1251px;width:72px;height:44px;background:#2b8fb3">
  <svg width="22" height="22" viewBox="0 0 24 24" fill="none" stroke="#fff" stroke-width="1.8"><path d="M8 6a8 8 0 0 0 0 12M12 9a4 4 0 0 0 0 6M4 3a12 12 0 0 0 0 18"/></svg>
</div>
<div class="owl-badge" style="left:983px;top:1271px;width:110px;height:110px"><div class="mascot" role="img" aria-label="Owl mascot"></div></div>

<!-- 03 Text -->
<div class="dots" style="left:360px;top:2000px;width:254px;height:170px;border-left:none;border-top:none"></div>
<div class="media" role="img" aria-label="Smiling man in a suit reading his phone" style="left:108px;top:1805px;width:479px;height:327px;background:radial-gradient(ellipse 22% 30% at 30% 38%,#c9a48c 0%,#9b7766 50%,transparent 80%),linear-gradient(100deg,#2c333b 0%,#3a434d 35%,#7f8b95 60%,#b9c5cc 100%)"></div>
<div class="chat-card" style="left:413px;top:1900px;width:219px;height:137px;display:flex;align-items:center;justify-content:center;gap:18px">
  <svg width="84" height="76" viewBox="0 0 84 76"><ellipse cx="36" cy="30" rx="34" ry="26" fill="#fff"/><path d="M14 48l-6 16 18-10z" fill="#fff"/><ellipse cx="56" cy="50" rx="22" ry="17" fill="#d7eef5"/><path d="M20 22h32M20 32h32M20 42h20" stroke="#2b9bb4" stroke-width="3"/></svg>
  <div class="mascot" role="img" aria-label="Owl mascot" style="position:relative;width:56px;height:80px"></div>
</div>
<div class="abs num" style="left:699px;top:1819px">03</div>
<div class="abs feat-title" style="left:699px;top:1853px">Text</div>
<div class="abs rule" style="left:699px;top:1908px"></div>
<div class="abs feat-name" style="left:699px;top:1947px">ovaMerrit</div>
<div class="abs feat-desc" style="left:699px;top:1982px">responds to my text messages</div>
<div class="btn" style="left:699px;top:2042px;width:195px;height:58px">
  <span class="arrow"><svg width="14" height="14" viewBox="0 0 14 14"><path d="M2 7h10M8 3l4 4-4 4" stroke="#333" stroke-width="1.6" fill="none"/></svg></span>Try Out Text
</div>

<!-- 04 Email -->
<div class="abs num" style="left:103px;top:2303px">04</div>
<div class="abs feat-title" style="left:103px;top:2332px">Email</div>
<div class="abs rule" style="left:103px;top:2388px"></div>
<div class="abs feat-name" style="left:103px;top:2424px">Merrit</div>
<div class="abs feat-desc" style="left:103px;top:2461px">responds to my emails</div>
<div class="btn" style="left:103px;top:2521px;width:197px;height:58px">
  <span class="arrow"><svg width="14" height="14" viewBox="0 0 14 14"><path d="M2 7h10M8 3l4 4-4 4" stroke="#333" stroke-width="1.6" fill="none"/></svg></span>Try Out Mail
</div>
<div class="dots" style="left:566px;top:2330px;width:524px;height:362px;border-top:none;border-right:none"></div>
<div class="media" role="img" aria-label="Person holding a phone with red email envelopes floating above it" style="left:592px;top:2313px;width:480px;height:326px;background:radial-gradient(ellipse 30% 26% at 52% 30%,rgba(214,74,86,.55) 0%,transparent 80%),radial-gradient(ellipse 22% 20% at 80% 85%,#c99e82 0%,transparent 90%),linear-gradient(110deg,#e2e3e5 0%,#b4bbc5 18%,#4f6a8f 42%,#34496b 75%,#2b3c58 100%)"></div>
<div class="icon-tile" style="left:471px;top:2375px;width:93px;height:76px;background:linear-gradient(120deg,#2b9bb4,#5a6fb0)">
  <svg width="52" height="40" viewBox="0 0 52 40"><rect x="2" y="8" width="48" height="30" rx="2" fill="#e9eef5"/><path d="M2 10l24 16 24-16" stroke="#9aa8bb" stroke-width="2" fill="none"/><circle cx="26" cy="10" r="9" fill="#2b82c9"/><text x="26" y="14" font-size="11" fill="#fff" text-anchor="middle" font-family="Inter,sans-serif">@</text></svg>
</div>
<div class="owl-badge" style="left:546px;top:2415px;width:116px;height:116px"><div class="mascot" role="img" aria-label="Owl mascot"></div></div>

<!-- 05 Leads -->
<div class="dots" style="left:330px;top:3060px;width:258px;height:150px;border-left:none;border-top:none"></div>
<div class="device" style="left:110px;top:2832px;width:444px;height:338px">
  <div class="fill" role="img" aria-label="Hand holding a glowing network of contact icons" style="background:radial-gradient(circle at 50% 54%,#ffffff 0%,#aee6f7 7%,#3aa3d6 14%,#6f7f8c 30%,#3b3f45 62%,#1f2226 100%)"></div>
</div>
<div class="abs num" style="left:697px;top:2799px">05</div>
<div class="abs feat-title" style="left:697px;top:2828px">Manage My Leads</div>
<div class="abs rule" style="left:697px;top:2883px"></div>
<div class="abs feat-name" style="left:699px;top:2920px">ovaMerrit</div>
<div class="abs feat-desc" style="left:699px;top:2953px;width:410px;line-height:38.5px">Manage my leads and ensure that I always follow up with the most qualified leads as quickly as possible</div>
<div class="btn" style="left:699px;top:3102px;width:246px;height:58px">
  <span class="arrow"><svg width="14" height="14" viewBox="0 0 14 14"><path d="M2 7h10M8 3l4 4-4 4" stroke="#333" stroke-width="1.6" fill="none"/></svg></span>Manage My Leads
</div>

<!-- CTA -->
<section class="cta">
  <h2>Set Up Your Own Merrit</h2>
  <div class="rule"></div>
  <div class="btn" style="left:456px;top:211px;width:288px;height:58px;justify-content:center;padding-left:0">
    <span class="arrow"><svg width="14" height="14" viewBox="0 0 14 14"><path d="M2 7h10M8 3l4 4-4 4" stroke="#333" stroke-width="1.6" fill="none"/></svg></span>Sign Up Now
  </div>
</section>
<div class="mascot" role="img" aria-label="Blue owl mascot with round glasses" style="left:540px;top:3640px;width:120px;height:160px"></div>

<!-- Footer -->
<footer>
  <div class="abs brand footer-brand">ovaMerrit!</div>
  <nav class="footer-nav">
    <a href="#" style="left:451px">Home</a>
    <a href="#" style="left:544px">About</a>
    <a href="#" style="left:641px">News &amp; Blog</a>
  </nav>
  <div class="social" style="left:448px" aria-label="Professional network">Pro</div>
  <div class="social" style="left:526px" aria-label="Photo network">Pics</div>
  <div class="social" style="left:604px" aria-label="Video network">Clips</div>
  <div class="social" style="left:682px" aria-label="Friends network">Friends</div>
  <div class="abs feedback">Have feedback? <span>Let us know!</span></div>
  <div class="abs legal" style="left:106px">© 2024 <b>ovaMerrit.</b> All right reserved, Privacy Policy &nbsp;|&nbsp; Terms Of Use</div>
  <div class="abs stamp">January 12,2024. Layout_2</div>
</footer>

</body>
</html>
```